Redesign of 2 real estate websites!

We need a redesign of our two real estate websites. These websites offer detailed information on the two real estates and need a modern fresh up.
Both websites should have the same design type, so you can see that they belong together, yet they should be in different colors. There is no logo to these pages, so the headlines can be integreated into the designs.
http://www.lindqvar-villa.de
http://www.osmund-lindqvar-haus.de/

```html
<!DOCTYPE html>
<html lang="en">
<head>
<meta charset="utf-8">
<title>Die Lindqvar-Villa</title>
<link href="https://fonts.googleapis.com/css2?family=Arimo:wght@400;700&display=swap" rel="stylesheet">
<style>
:root{
  --green-dark:#053a05;
  --green-nav:#0d540d;
  --green-nav-light:#166d16;
  --green-active:#0a3f0a;
  --green-head:#0e4a0e;
  --text:#555;
  --text-light:#666;
  --rule:#d6d6d6;
  --grey-band:#ebebeb;
  --white:#fff;
}
*{margin:0;padding:0;box-sizing:border-box}
html,body{width:975px;height:1200px;overflow:hidden}
body{font-family:Arimo,Arial,sans-serif;background:var(--white);color:var(--text);position:relative}
.abs{position:absolute}
.header{left:0;top:0;width:975px;height:66px;background:var(--green-dark)}
.brand{left:140px;top:18px;font-size:26px;color:var(--white);font-weight:400;letter-spacing:.5px}
.contact{font-size:9px;color:var(--white);display:flex;align-items:center;gap:5px;white-space:nowrap}
.lang{left:764px;top:21px;width:73px;height:21px;border:1px solid var(--white);font-size:8px;color:var(--white);display:flex;align-items:center;padding-left:6px;gap:5px}
.flag{width:13px;height:9px;background:#2a3f8f;border:1px solid #c33}
.nav{left:0;top:66px;width:975px;height:35px;background:linear-gradient(var(--green-nav-light),var(--green-nav));display:flex;padding-left:140px}
.nav a{color:var(--white);font-size:10px;text-decoration:none;height:35px;line-height:35px;padding:0 25px 0 28px;white-space:nowrap}
.nav a.active{background:var(--green-active)}
.slider{left:140px;top:119px;width:697px;height:270px;background:linear-gradient(180deg,#c9d1d6 0%,#9b5a46 45%,#7a3b2e 75%,#5b4a3a 100%)}
.cap{background:rgba(0,0,0,.75);color:var(--white);font-size:11.5px;padding:0 15px;height:32px;line-height:32px;white-space:nowrap}
.arrows{display:flex;gap:2px}
.arrows span{width:19px;height:19px;background:rgba(80,80,80,.7);color:#ddd;font-size:10px;text-align:center;line-height:19px}
.arrows.small span{width:12px;height:11px;line-height:11px;font-size:8px;background:#777;color:#fff}
.intro-title{left:145px;top:411px;font-size:12px;color:var(--green-head);white-space:nowrap}
.intro-text{left:146px;top:435px;font-size:10px;color:var(--text-light);white-space:nowrap}
.btn{left:682px;top:413px;width:152px;height:33px;border-radius:17px;background:linear-gradient(#1d6a1d,#053a05);color:var(--white);font-size:14px;text-align:center;line-height:33px}
.rule{left:140px;top:468px;width:697px;height:1px;background:var(--rule)}
h2{position:absolute;font-weight:400;font-size:15px;color:var(--green-head);white-space:nowrap}
.body-text{left:140px;width:475px;font-size:8px;line-height:16.8px;color:var(--text-light)}
.frame{border:1px solid #ddd;padding:4px;background:var(--white)}
.ph{width:100%;height:100%}
.villa h3{font-size:10px;font-weight:400;color:var(--green-head);margin-top:14px}
.villa p{font-size:8px;line-height:15.5px;color:var(--text-light);margin-top:6px;width:160px}
.band{left:0;top:896px;width:975px;height:226px;background:var(--grey-band)}
.post{display:flex;gap:13px;width:220px}
.post .frame{width:56px;height:48px;padding:3px;flex:none}
.post h4{font-size:10px;font-weight:400;color:var(--green-head)}
.post p{font-size:8px;color:var(--text-light);margin-top:7px;white-space:nowrap}
.post em{display:block;font-size:7px;color:var(--green-head);font-weight:700;margin-top:6px}
.footer{left:0;top:1122px;width:975px;height:78px;background:var(--green-dark)}
.flinks{left:140px;top:1147px;font-size:7.5px;color:var(--white);word-spacing:1px;white-space:nowrap}
.flinks span{margin:0 7px}
.copy{left:140px;top:1169px;font-size:7px;color:var(--white)}
.social{left:693px;top:1150px;display:flex;gap:7px}
.social span{width:23px;height:23px;border-radius:50%;background:#6d8a6d;display:block}
</style>
</head>
<body>
<div class="abs header"></div>
<div class="abs brand">Die Lindqvar-Villa</div>
<div class="abs contact" style="left:556px;top:18px">
  <svg width="9" height="7" viewBox="0 0 9 7"><rect x=".5" y=".5" width="8" height="6" fill="none" stroke="#fff"/><path d="M.5 .5L4.5 4L8.5 .5" fill="none" stroke="#fff"/></svg>
  kontakt@lindqvar-villa
  <svg width="6" height="10" viewBox="0 0 6 10" style="margin-left:9px"><rect x=".5" y=".5" width="5" height="9" rx="1" fill="none" stroke="#fff"/></svg>
  ( 1021 ) 555 0142
</div>
<div class="abs contact" style="left:556px;top:40px">
  <svg width="7" height="9" viewBox="0 0 7 9"><path d="M3.5 9C1 5.5 0 4.5 0 3.2A3.5 3.5 0 0 1 7 3.2C7 4.5 6 5.5 3.5 9Z" fill="#fff"/><circle cx="3.5" cy="3.3" r="1.2" fill="#053a05"/></svg>
  102 Street name, State name, Country
</div>
<div class="abs lang"><span class="flag"></span>English <svg width="7" height="5" viewBox="0 0 7 5" style="margin-left:6px"><path d="M1 1L3.5 3.5L6 1" fill="none" stroke="#fff"/></svg></div>

<nav class="abs nav">
  <a class="active">Mittweida</a><a>Building design</a><a>Owners and Residents</a><a>The villa</a><a>Links / Directions</a><a>Imprint</a><a>Rental</a>
</nav>

<div class="abs slider" role="img" aria-label="Photo of the red brick villa with tower and yellow neighbouring house"></div>
<div class="abs cap" style="left:143px;top:297px;height:33px;line-height:33px">DIE LINDQVAR VILLA</div>
<div class="abs cap" style="left:143px;top:333px">ELECTRICALLY CONTROLLED DOOR SYSTEM WITH REMOTE CONTROL</div>
<div class="abs arrows" style="left:782px;top:356px"><span>&lsaquo;</span><span>&rsaquo;</span></div>

<div class="abs intro-title">Der Landkreis Mittelsachsen ist ein Landkreis im Freistaat Sachsen.</div>
<div class="abs intro-text">Der Landkreis Mittelsachsen ist ein Landkreis im Freistaat Sachsen. Wirtschaftlich betrachtet befindet sich dieser</div>
<div class="abs btn">Contact now</div>
<div class="abs rule"></div>

<h2 style="left:140px;top:486px">Welcome to Die Lindqvar Villa</h2>
<div class="abs body-text" style="top:512px">
  <p>The district is a district in Central Saxony Free State of Saxony. In economic terms, there is this county in the so-called Saxon triangle between Dresden, Leipzig and Chemnitz. It is characterized industrially and agriculturally. The gutter county seat region has a very well developed through the nearby connections to the A4 highway with the directions Dresden, Leipzig, Berlin and Chemnitz and convenient connections by train and bus.</p>
  <p style="margin-top:16.8px">The large district Mittweida with the university established in 1867, is located not far from Chemnitz to the recreation area of Kriebstein. Your special appeal is the large county town of the historic facilities...</p>
</div>
<div class="abs frame" style="left:641px;top:498px;width:196px;height:124px"><div class="ph" role="img" aria-label="Photo of the villa front with parked cars" style="background:linear-gradient(#5f8a4c,#9b5a46 55%,#888)"></div></div>

<h2 style="left:140px;top:657px">Recent Villas</h2>
<div class="abs arrows small" style="left:810px;top:660px"><span>&lsaquo;</span><span>&rsaquo;</span></div>

<div class="abs villa" style="left:140px;top:693px">
  <div class="frame" style="width:163px;height:111px"><div class="ph" role="img" aria-label="Photo of the villa driveway" style="background:linear-gradient(90deg,#4e7a3a,#a5604c 40%,#c8a08c)"></div></div>
  <h3>Zufahrt</h3><p>Electrically controlled door system with remote control</p>
</div>
<div class="abs villa" style="left:317px;top:693px">
  <div class="frame" style="width:163px;height:111px"><div class="ph" role="img" aria-label="Photo of the tower terrace" style="background:linear-gradient(#cfd6da,#9a4b36 45%,#7c3a2b)"></div></div>
  <h3>Turmterrasse</h3><p>Electrically controlled door system with remote control</p>
</div>
<div class="abs villa" style="left:495px;top:693px">
  <div class="frame" style="width:163px;height:111px"><div class="ph" role="img" aria-label="Photo of the town square with historic houses" style="background:linear-gradient(#b9c6d2,#d0b48a 50%,#8a8278)"></div></div>
  <h3>Hauseingang</h3><p>Electrically controlled door system with remote control</p>
</div>
<div class="abs villa" style="left:673px;top:693px">
  <div class="frame" style="width:164px;height:111px"><div class="ph" role="img" aria-label="Photo of the garage seen from the garden" style="background:linear-gradient(#c7ccd0,#e8d8d4 45%,#6a4a40)"></div></div>
  <h3>Blick vom Garten</h3><p>Electrically controlled door system with remote control</p>
</div>

<div class="abs band"></div>
<h2 style="left:140px;top:921px">Recent Posts</h2>
<div class="abs arrows small" style="left:810px;top:925px"><span>&lsaquo;</span><span>&rsaquo;</span></div>

<div class="abs post" style="left:140px;top:954px"><div class="frame"><div class="ph" role="img" aria-label="Post photo of the villa" style="background:linear-gradient(#6f8f5a,#9a5a44)"></div></div><div><h4>Turmterrasse</h4><p>Electrically controlled door with &nbsp;system</p><em>Posted on 27 Mar 2014</em></div></div>
<div class="abs post" style="left:384px;top:954px"><div class="frame"><div class="ph" role="img" aria-label="Post photo of the garage" style="background:linear-gradient(#c9cfd3,#d8c9c2 50%,#6c7a5a)"></div></div><div><h4>Turmterrasse</h4><p>Electrically controlled door with &nbsp;system</p><em>Posted on 27 Mar 2014</em></div></div>
<div class="abs post" style="left:621px;top:954px"><div class="frame"><div class="ph" role="img" aria-label="Post photo of the garden path" style="background:linear-gradient(#b8c2b0,#5f8a44)"></div></div><div><h4>Turmterrasse</h4><p>Electrically controlled door with &nbsp;system</p><em>Posted on 27 Mar 2014</em></div></div>
<div class="abs post" style="left:140px;top:1032px"><div class="frame"><div class="ph" role="img" aria-label="Post photo of the garden trees" style="background:linear-gradient(#a9b8b0,#4f7a3a)"></div></div><div><h4>Turmterrasse</h4><p>Electrically controlled door with &nbsp;system</p><em>Posted on 27 Mar 2014</em></div></div>
<div class="abs post" style="left:384px;top:1032px"><div class="frame"><div class="ph" role="img" aria-label="Post photo of the tower" style="background:linear-gradient(#cfd6da,#94462f)"></div></div><div><h4>Turmterrasse</h4><p>Electrically controlled door with &nbsp;system</p><em>Posted on 27 Mar 2014</em></div></div>
<div class="abs post" style="left:621px;top:1032px"><div class="frame"><div class="ph" role="img" aria-label="Post photo of the garden steps" style="background:linear-gradient(#7c8f6a,#4a4a40)"></div></div><div><h4>Turmterrasse</h4><p>Electrically controlled door with &nbsp;system</p><em>Posted on 27 Mar 2014</em></div></div>

<div class="abs footer"></div>
<div class="abs flinks">Home<span>|</span>Mittweida<span>|</span>Building design<span>|</span>Owners and Residents<span>|</span>The villa<span>|</span>Links / Directions<span>|</span>Imprint<span>|</span>Rental<span>|</span>Contact</div>
<div class="abs copy">Copyrights © 2014. Die Lindqvar Villa. All Rights Reserved.</div>
<div class="abs social"><span></span><span></span><span></span><span></span><span></span></div>
</body>
</html>
```